Business Telephone Service Brochure

I need a brochure designed to help sell our VoIP service. The brochure needs to be clean, attention getting, professional and have 3 key areas of information (Key Features, Benefits & Service Plans). Here is an idea of what we are looking for https://www.artflockly.com/design/52930487. Need to also include how much the customer could save. See this for an example https://42mockups.com/postcard-flyer-design/contests/voip-sales-flyer-template-replicate-attached-358209. The Service Plan section needs to allow room for two types of plans. One plan includes the phone and has a 12, 24 and 36 month option. Each term (12,24,36) will have its own monthly cost per device. The second service option is no-commitment monthly with a single per month price per device. The included features section should allow for up to 16 features to be listed. The benefits should allow for 4-6 benefits to be listed. Also include room for Logo, business address, website, phone number and email.

Target Market(s)

Small to medium business with 1-100 employees.

Industry/Entity Type

Telecommunications

Font styles to use
Serif

Colors

Designer to choose colors to be used in the design.

Requirements
Must have
• Key Feature, Benefits and Service Plans (i.e. Pricing). Company logo, phone, email and website. Must have "Save up to x%!" and catch attention.
Nice to have
• Limited colors. I am not setting a hard limit, please take the liberty to do what you feel is needed. Just keep in mind we want it to be clean, professional and attention getting without being to flashy or obnoxious.
Should not have
• Nothing busy or distracting.

```html
<!DOCTYPE html>
<html lang="en">
<head>
<meta charset="utf-8">
<title>nexlo – Business Telephone Service Flyer</title>
<link href="https://fonts.googleapis.com/css2?family=Lato:wght@400;700;900&display=swap" rel="stylesheet">
<style>
:root{
  --navy:#262f7e;
  --navy-deep:#1d2160;
  --blue:#1a6cb5;
  --blue-mid:#1b58a4;
  --royal:#28389a;
  --line-blue:#2a7fd0;
  --paper:#efeff1;
  --grey:#7a7a7c;
  --grey-cell:#b9b9bd;
  --text:#555559;
  --charcoal:#2b2c30;
  --stage:#dcdde0;
}
*{box-sizing:border-box;margin:0;padding:0}
html,body{width:1200px;height:800px;overflow:hidden;background:var(--stage);font-family:'Lato',sans-serif}
.page{position:absolute;top:30px;width:524px;height:740px;background:var(--paper);overflow:hidden;box-shadow:0 6px 18px rgba(0,0,0,.18)}
.page--front{left:60px}
.page--back{left:616px;width:528px}
.page svg.bg{position:absolute;left:0;top:0}
.abs{position:absolute}

/* front */
.brand{left:312px;top:8px;font-size:84px;font-weight:900;color:var(--navy);letter-spacing:-2px;line-height:1}
.brand-tag{left:314px;top:97px;font-size:10px;color:var(--navy);letter-spacing:.1px;white-space:nowrap}
.headline{right:24px;top:158px;text-align:right}
.headline h2{font-size:30px;font-weight:900;color:var(--navy);line-height:1}
.headline p{font-size:19px;color:#fff;margin-top:8px}
.pill-outline{border:2px solid #fff;border-radius:16px;color:#fff;text-align:center}
.plans-pill{left:26px;top:318px;width:186px;height:30px;font-size:17px;line-height:26px}
.plans{left:30px;top:374px;width:198px;color:#fff;font-size:10.5px;line-height:1.42;list-style:none}
.plans li{position:relative;padding-left:16px;margin-bottom:12px}
.plans li::before{content:"➤";position:absolute;left:0;font-size:8px;top:2px}
.plans li.cont{margin-top:-6px}
.plans li.cont::before{content:""}
.plans b{font-size:13px;font-weight:700}
.benefits-pill{left:264px;top:293px;width:126px;height:22px;background:var(--navy);border-radius:11px;color:#fff;font-size:14px;text-align:center;line-height:22px}
.benefits{left:264px;top:323px;list-style:none;font-size:10.5px;color:var(--text)}
.benefits li{height:19.6px;padding-left:14px;position:relative;white-space:nowrap}
.benefits li::before{content:"➤";position:absolute;left:0;font-size:8px;top:1px;color:var(--navy)}
.call{left:250px;top:530px;width:240px;text-align:center;font-size:22px;font-weight:900;color:var(--navy);letter-spacing:1.2px}
.phone-pill{left:280px;top:568px;width:180px;height:28px;background:var(--navy);border-radius:14px;color:#fff;font-size:16px;letter-spacing:.5px;display:flex;align-items:center;justify-content:center;gap:6px;white-space:nowrap}
.phone-pill svg{flex:none}
.rule{left:254px;top:614px;width:226px;height:2px;background:var(--navy)}
.address{left:294px;top:628px;font-size:13px;color:var(--grey);line-height:1.15;letter-spacing:.6px}
.address-pin{left:270px;top:630px}
.web{left:290px;top:718px;color:#fff;font-size:11px;letter-spacing:.8px;display:flex;align-items:center;gap:8px;white-space:nowrap}

/* back */
.kf-pill{left:168px;top:21px;width:190px;height:32px;font-size:21px;line-height:27px;letter-spacing:1.5px}
.feature{display:flex;align-items:center;gap:10px;color:#e6e6ea;font-size:8.2px;letter-spacing:.5px;line-height:1.55;width:200px}
.feature i{flex:none;width:22px;height:22px;border-radius:50%;background:#fff;display:flex;align-items:center;justify-content:center}
.feature i::after{content:"";width:9px;height:9px;border-radius:50%;background:var(--navy)}
.service-title{left:50px;top:386px;font-size:24px;font-weight:900;color:var(--navy);letter-spacing:1.5px}
.price-table{left:50px;top:391px;border-collapse:separate;border-spacing:0;font-size:8.5px;letter-spacing:.6px;color:#fff}
.price-table th{height:26px;background:var(--navy);font-weight:400;font-size:9.5px;padding:0 4px;white-space:nowrap}
.price-table td{height:32px;text-align:center}
.price-table tr.gap td{height:6px;background:none!important}
.price-table .label{width:110px;background:var(--grey-cell);color:#333;text-align:left;padding-left:4px;font-size:7.6px;line-height:1.45}
.price-table .c1{width:62px;background:var(--blue)}
.price-table .c2{width:85px;background:var(--blue-mid)}
.price-table .c3{width:84px;background:var(--royal)}
.price-table .c4{width:84px;background:var(--navy-deep)}
.price-table th.blank{background:none;width:110px}
.note{left:55px;width:430px;font-size:10.5px;color:var(--text);letter-spacing:.7px;line-height:1.4}
.save{color:#fff;line-height:1;white-space:nowrap}
.save-word{left:258px;top:646px;font-size:24px}
.save-upto{left:192px;top:706px;font-size:22px}
.save-num{left:264px;top:662px;font-size:72px;letter-spacing:-2px}
</style>
</head>
<body>

<section class="page page--front">
  <svg class="bg" width="524" height="740" viewBox="0 0 524 740">
    <defs>
      <linearGradient id="teamTone" x1="0" y1="0" x2="1" y2="1">
        <stop offset="0" stop-color="#c9ccd3"/><stop offset="1" stop-color="#8d929c"/>
      </linearGradient>
      <linearGradient id="deskTone" x1="0" y1="0" x2="0" y2="1">
        <stop offset="0" stop-color="#f4f4f4"/><stop offset="1" stop-color="#c8c9cc"/>
      </linearGradient>
    </defs>
    <rect x="0" y="0" width="330" height="310" fill="url(#teamTone)" role="img" aria-label="Photo of call-centre agents wearing headsets at their desks"/>
    <polygon points="305,135 524,135 524,272 318,272" fill="#7b7b7d"/>
    <path d="M0,305 C150,250 380,240 524,285 L524,520 L240,520 C236,545 215,556 190,556 L0,556 Z" fill="var(--navy)"/>
    <path d="M0,302 C150,246 380,236 524,281" fill="none" stroke="var(--line-blue)" stroke-width="2"/>
    <path d="M250,300 C350,284 450,300 524,335 L524,466 L250,466 Z" fill="var(--paper)"/>
    <circle cx="330" cy="468" r="25" fill="#5f86b8" stroke="#fff" stroke-width="2" role="img" aria-label="Photo of a telecom tower"/>
    <circle cx="430" cy="468" r="25" fill="#c8b9a8" stroke="#fff" stroke-width="2" role="img" aria-label="Photo of a woman on the phone"/>
    <path d="M0,670 L200,670 L240,712 L524,712 L524,740 L0,740 Z" fill="var(--navy)"/>
    <rect x="15" y="575" width="140" height="160" rx="10" fill="url(#deskTone)" role="img" aria-label="Photo of a white desk telephone"/>
  </svg>

  <div class="abs brand">nexlo</div>
  <div class="abs brand-tag">Internet-Telephone-Security-Networking</div>
  <div class="abs headline"><h2>WE HELP</h2><p>PEOPLE CONNECT</p></div>

  <div class="abs pill-outline plans-pill">OUR PLANS</div>
  <ul class="abs plans">
    <li>One plan includes the phone and has a <b>12, 24</b> and <b>36</b> month option.</li>
    <li class="cont">Each term <b>(12,24,36)</b> will have its own monthly cost per device.</li>
    <li>The second service option is no-commitment monthly with a single per <b>month price</b> per device.</li>
  </ul>

  <div class="abs benefits-pill">Benefits</div>
  <ul class="abs benefits">
    <li>No expensive onsite telephone equipment</li>
    <li>Easily scale up or down and needs changet</li>
    <li>Free telephone/email support</li>
    <li>Lower monthly cost</li>
    <li>Increase reliability</li>
    <li>Easy self-administration</li>
  </ul>

  <div class="abs call">CALL US TODAY</div>
  <div class="abs phone-pill">
    <svg width="14" height="14" viewBox="0 0 24 24"><path fill="#fff" d="M6.6 10.8a15 15 0 0 0 6.6 6.6l2.2-2.2c.3-.3.7-.4 1-.2 1.1.4 2.3.6 3.6.6.6 0 1 .4 1 1V20c0 .6-.4 1-1 1A17 17 0 0 1 3 4c0-.6.4-1 1-1h3.5c.6 0 1 .4 1 1 0 1.3.2 2.5.6 3.6.1.3 0 .7-.2 1z"/></svg>
    <span>+1 555 014 288</span>
  </div>
  <div class="abs rule"></div>
  <svg class="abs address-pin" width="14" height="16" viewBox="0 0 14 16"><circle cx="7" cy="7" r="6" fill="none" stroke="var(--navy)" stroke-width="1.6"/><circle cx="7" cy="7" r="2" fill="var(--navy)"/></svg>
  <div class="abs address">Abcdeyewjd,<br>djdsdhgkfljulkdk,<br>fhjhdyudhsjdklsiedj</div>
  <div class="abs web">
    <svg width="13" height="13" viewBox="0 0 14 14" fill="none" stroke="#fff" stroke-width="1"><circle cx="7" cy="7" r="6"/><ellipse cx="7" cy="7" rx="2.6" ry="6"/><path d="M1 7h12M2 4h10M2 10h10"/></svg>
    www.nexlovoice.com
  </div>
</section>

<section class="page page--back">
  <svg class="bg" width="528" height="740" viewBox="0 0 528 740">
    <defs>
      <radialGradient id="darkTone" cx=".5" cy=".4" r=".8">
        <stop offset="0" stop-color="#3a3b40"/><stop offset="1" stop-color="#222326"/>
      </radialGradient>
      <linearGradient id="lockTone" x1="0" y1="0" x2="1" y2="0">
        <stop offset="0" stop-color="#0e1420"/><stop offset=".5" stop-color="#1e4a6e"/><stop offset="1" stop-color="#0e1420"/>
      </linearGradient>
    </defs>
    <path d="M0,0 H528 V300 C380,335 160,335 0,270 Z" fill="url(#darkTone)" role="img" aria-label="Dark world map background with radiating light rays"/>
    <path d="M0,270 C160,335 380,335 528,300 L528,306 C380,372 160,372 0,318 Z" fill="var(--navy)"/>
    <path d="M0,318 C160,372 380,372 528,306" fill="none" stroke="var(--line-blue)" stroke-width="1.5"/>
    <path d="M0,675 C150,615 380,605 528,640 L528,740 L0,740 Z" fill="var(--navy)"/>
    <path d="M0,690 C150,650 380,642 528,680 L528,740 L0,740 Z" fill="url(#lockTone)" role="img" aria-label="Digital security padlock over glowing data background"/>
  </svg>

  <div class="abs pill-outline kf-pill">Key Features</div>

  <div class="abs feature" style="left:54px;top:62px"><i></i><span>Unlimited local and long<br>distance calling</span></div>
  <div class="abs feature" style="left:54px;top:99px"><i></i><span>HD Voice</span></div>
  <div class="abs feature" style="left:54px;top:134px"><i></i><span>Business SMS/Text Messaging</span></div>
  <div class="abs feature" style="left:54px;top:171px"><i></i><span>Personal and Shared Voicemail Boxes</span></div>
  <div class="abs feature" style="left:54px;top:206px"><i></i><span>Audio Conferencing</span></div>
  <div class="abs feature" style="left:54px;top:243px"><i></i><span>Intercom</span></div>

  <div class="abs feature" style="left:296px;top:62px"><i></i><span>Mobile App</span></div>
  <div class="abs feature" style="left:296px;top:100px"><i></i><span>Auto Attendant/Interactive<br>Voice Routing</span></div>
  <div class="abs feature" style="left:296px;top:134px"><i></i><span>Free web or email fax</span></div>
  <div class="abs feature" style="left:296px;top:171px"><i></i><span>Web admin portal</span></div>
  <div class="abs feature" style="left:296px;top:207px"><i></i><span>Music On Hold - Customizable</span></div>
  <div class="abs feature" style="left:296px;top:243px"><i></i><span>Simultaneous ring / follow-me</span></div>
  <div class="abs feature" style="left:296px;top:280px"><i></i><span>Redundancy/Failover –<br>Never miss a call</span></div>

  <div class="abs service-title">SERVICE</div>
  <table class="abs price-table">
    <tr><th class="blank"></th><th class="c1">Monthly</th><th class="c2">12 month term</th><th class="c3">24 month term</th><th class="c4">36 month term</th></tr>
    <tr class="gap"><td colspan="5"></td></tr>
    <tr><td class="label">¹Phone service only<br>(phone sold separately)</td><td class="c1">$21.95</td><td class="c2"></td><td class="c3"></td><td class="c4"></td></tr>
    <tr class="gap"><td colspan="5"></td></tr>
    <tr><td class="label">Service + ²Tellaro<br>T20 Phone</td><td class="c1"></td><td class="c2">$24.95</td><td class="c3">$22.95</td><td class="c4">$20.95</td></tr>
  </table>

  <p class="abs note" style="top:524px">¹For monthly service you may purchase the Tellaro T20 phone for $65 each, less taxes and shipping.</p>
  <p class="abs note" style="top:565px">²Tellaro T20 phones are rented and due upon cancellation. Customer pays return shipping.</p>

  <div class="abs save save-word">SAVE</div>
  <div class="abs save save-upto">UP TO</div>
  <div class="abs save save-num">70%</div>
</section>

</body>
</html>
```